Brightwell Harbor Property Maintenance and Construction Company require new business card design

We are a property maintenance and construction company that offer a total range of property maintenance construction services and have been too busy dealing with the running of the office and completing jobs to update our business cards. We have recently had a new logo designed for us and are needing to update our cards (and we also have new staff requiring business cards. We would ideally want to stay with the orange, black and grey theme. I have attached current business cards and also our new logo. Looking forward to feedback and ideas.

Target Market(s)

Real estate agents, local governments, companies, residential

Industry/Entity Type

Property Maintenance

Contact Information for Business Card

File uploaded has names and phone numbers for staff. We also need to add a card for a new staff member, which can be provided.

Colors
f37022

Requirements
Must have
• Must have logos for Certified Fabrication Steward and Prime Erector for which we are members of. Also a description of what services we provide
Should not have
• any "flowery" fonts and design. We are a construction company, so probably something very standard...but also not just a regular font (ie Arial!)

```html
<!DOCTYPE html>
<html lang="en">
<head>
<meta charset="utf-8">
<title>Brightwell Harbor – Business Card</title>
<link href="https://fonts.googleapis.com/css2?family=Exo+2:wght@400;600;700&family=Open+Sans:wght@400;600&display=swap" rel="stylesheet">
<style>
  :root {
    --orange: #f37022;
    --orange-deep: #e9631a;
    --grey: #5c5f63;
    --ink: #1e1e1e;
    --white: #ffffff;
    --paper: #ecebe8;
  }
  * { box-sizing: border-box; margin: 0; padding: 0; }
  html, body { width: 1200px; height: 900px; overflow: hidden; }
  body {
    background: var(--paper);
    font-family: "Open Sans", Arial, sans-serif;
    position: relative;
  }
  .card {
    position: absolute;
    left: 240px;
    width: 720px;
    height: 410px;
    overflow: hidden;
    box-shadow: 0 6px 18px rgba(0,0,0,.18);
  }

  /* ---------- Front ---------- */
  .card-front { top: 30px; background: var(--white); }
  .front-top-band { position: absolute; left: 0; top: 0; width: 100%; height: 34px; background: var(--grey); }
  .front-top-rule { position: absolute; left: 0; top: 40px; width: 100%; height: 3px; background: var(--orange); }
  .front-bottom-band { position: absolute; left: 0; bottom: 0; width: 100%; height: 44px; background: var(--orange); }

  .brand-lockup {
    position: absolute; left: 44px; top: 172px;
    display: flex; align-items: center; gap: 10px;
  }
  .brand-square { width: 22px; height: 22px; background: var(--orange); }
  .brand-name {
    font-family: "Exo 2", sans-serif; font-weight: 700; font-size: 30px;
    color: var(--ink); letter-spacing: .5px;
  }
  .licence {
    position: absolute; left: 44px; top: 232px;
    font-family: "Exo 2", sans-serif; font-weight: 600; font-size: 16px;
    color: var(--orange); letter-spacing: 1.2px;
  }

  .contact-block { position: absolute; left: 420px; top: 86px; }
  .person-name {
    font-family: "Exo 2", sans-serif; font-weight: 700; font-size: 17px;
    color: var(--orange); letter-spacing: 1.5px;
  }
  .person-role { font-size: 13px; font-weight: 600; color: var(--ink); margin: 2px 0 10px; }
  .contact-list { list-style: none; }
  .contact-item {
    display: flex; align-items: center; gap: 10px;
    font-size: 12.5px; color: var(--ink); line-height: 19px;
  }
  .contact-icon { width: 11px; height: 11px; flex: none; }

  .member-badges {
    position: absolute; right: 34px; bottom: 60px;
    display: flex; gap: 16px; align-items: center;
  }
  .badge-round { width: 40px; height: 40px; border-radius: 50%; border: 3px solid #23407a; }
  .badge-block { width: 128px; height: 34px; background: #1d2b55; border-left: 34px solid #d8cc8a; }
  .badge-bar { width: 108px; height: 22px; background: #23407a; }

  /* ---------- Back ---------- */
  .card-back {
    top: 462px;
    background: linear-gradient(135deg, var(--orange) 0%, var(--orange-deep) 100%);
    color: var(--white);
    font-family: "Exo 2", sans-serif;
  }
  .back-heading {
    position: absolute; left: 34px; top: 28px;
    font-size: 23px; font-weight: 700; letter-spacing: 1.6px;
  }
  .service-list {
    position: absolute; list-style: none;
    font-size: 15.5px; font-weight: 600; letter-spacing: 1.1px; line-height: 21px;
  }
  .service-list-core { left: 34px; top: 80px; }
  .service-list-trades { right: 34px; top: 80px; text-align: right; }
  .service-list li { display: flex; align-items: center; gap: 10px; }
  .service-list-trades li { justify-content: flex-end; }
  .service-list-core li::before,
  .service-list-trades li::after {
    content: ""; width: 16px; height: 6px; background: var(--white); flex: none;
  }
  .service-list-trades li.no-mark::after { display: none; }

  .back-brand {
    position: absolute; left: 34px; bottom: 40px;
    display: flex; align-items: center; gap: 12px;
  }
  .back-brand .brand-square { width: 30px; height: 30px; background: var(--white); }
  .back-brand .brand-name { color: var(--white); font-size: 40px; }
  .address {
    position: absolute; right: 34px; bottom: 60px;
    font-family: "Open Sans", sans-serif; font-size: 14px; font-weight: 600;
  }
</style>
</head>
<body>

<section class="card card-front" aria-label="Business card front">
  <div class="front-top-band"></div>
  <div class="front-top-rule"></div>

  <div class="brand-lockup">
    <span class="brand-square"></span>
    <span class="brand-name">Brightwell Harbor</span>
  </div>
  <p class="licence">LICENCE NO. DB-U 47215</p>

  <div class="contact-block">
    <h1 class="person-name">DANA MERRICK</h1>
    <p class="person-role">Director</p>
    <ul class="contact-list">
      <li class="contact-item">
        <svg class="contact-icon" viewBox="0 0 12 12"><rect x="3" y="0.5" width="6" height="11" rx="1.2" fill="none" stroke="#f37022" stroke-width="1.4"/></svg>
        0400 555 217
      </li>
      <li class="contact-item">
        <svg class="contact-icon" viewBox="0 0 12 12"><path d="M2 1l2.5 0 1 3-1.5 1a7 7 0 0 0 3 3l1-1.5 3 1 0 2.5c-5 .5-9.5-4-9-9z" fill="#f37022"/></svg>
        1300 555 BWH (1300 555 294)
      </li>
      <li class="contact-item">
        <svg class="contact-icon" viewBox="0 0 12 12"><rect x="0.5" y="2" width="11" height="8" fill="#f37022"/><path d="M0.5 2l5.5 4.5 5.5-4.5" fill="none" stroke="#fff" stroke-width="1"/></svg>
        dana@brightwellharbor.example
      </li>
      <li class="contact-item">
        <svg class="contact-icon" viewBox="0 0 12 12"><circle cx="6" cy="6" r="5" fill="none" stroke="#f37022" stroke-width="1.4"/><path d="M1 6h10M6 1c-2.5 3-2.5 7 0 10M6 1c2.5 3 2.5 7 0 10" fill="none" stroke="#f37022" stroke-width="0.9"/></svg>
        www.brightwellharbor.example
      </li>
    </ul>
  </div>

  <div class="member-badges">
    <div class="badge-round" role="img" aria-label="Certified Fabrication Steward membership badge"></div>
    <div class="badge-bar" role="img" aria-label="Certified Fabrication Steward badge panel"></div>
    <div class="badge-block" role="img" aria-label="Prime Erector membership badge"></div>
  </div>

  <div class="front-bottom-band"></div>
</section>

<section class="card card-back" aria-label="Business card back">
  <h2 class="back-heading">OFFERING ALL PROPERTY MAINTENANCE SERVICES</h2>

  <ul class="service-list service-list-core">
    <li>PROGRAMMED MAINTENANCE</li>
    <li>ESSENTIAL SERVICES</li>
    <li>MAINTENANCE PLANNING</li>
    <li>REACTIONARY MAINTENANCE</li>
    <li>COMMERCIAL/RESIDENTIAL</li>
    <li>BODY CORPORATE</li>
    <li>INSURANCE CLAIMS</li>
    <li>24 HRS ON CALL</li>
  </ul>

  <ul class="service-list service-list-trades">
    <li>CARPENTRY</li>
    <li>PLUMBING</li>
    <li>ELECTRICAL</li>
    <li>PAINTING</li>
    <li>TILING</li>
    <li>PLASTERING</li>
    <li>GARDEN MAINTENANCE</li>
    <li>CLEANING SERVICES</li>
    <li>WATERPROOFING</li>
    <li class="no-mark">ALL HANDYMAN SERVICES</li>
  </ul>

  <div class="back-brand">
    <span class="brand-square"></span>
    <span class="brand-name">Brightwell Harbor</span>
  </div>
  <p class="address">42 Quarry Lane, Elmsford Vic 3999</p>
</section>

</body>
</html>
```